Harbor Wellness Partners -Postcard Design

New Post Card design for a new company based in Florida called "Harbor Wellness Partners". Our website is www.harborwellnesspartners-demo.com, our phone is 855-HARBR22 (855-427-2722). We offer a no fee service to help our clients find suitable alcohol/drug abuse/addition treatment so that they can attain LONG-TERM recovery.
The facilities we work with have been hand chosen by us after a rigorous interview process.
We have facilities that use various approaches to suit the needs of the client wanting Long-Term Recovery. Evidence based, 12-step based, christian based, and alternative healing based.
Feel free to add a "tag line" that you think will catch attention. We use..."We help our clients grow roots in Long-Term Recovery". "Call 1-855-HARBR22 before you have to call 911". "Long-Term recovery is our goal, not temporary sobriety."
We interview the treatment facilities to ensure that top treatment is given to our clients, we don't put there where they will not get the care promised.
Some services we can place for are: Interventions, Detox, Partial Hospitalization Program (PHP), Intensive Out Patient (IOP), Out Patient (OP), Sober Living Communities.
Several facilities with several approaches to treatment & recovery.
I have included our logo file for your use.

I am not a designer, so leaving entire design options open (eg...colors, graphics, fonts, etc....) Postcard size will be either 6 x 4 or 7 x 5.

Target Market(s)

Target Market for these postcards are treatment facilities & potential clients around the country. To give them someone to call for help in placing alcoholics & addicting into treatment facilities with different approaches.

Industry/Entity Type

It Company

Requirements
Must have
• THESE DO NOT HAVE TO BE EXACT WORDING!!
• The facilities we work with have been hand chosen by us after a rigorous interview process.
• Treatment programs: Detox, In-Patient, Partial Hospitalization Program (PHP), Intensive out patient (IOP), Out Patient, Sober Living Communities.
• We have facilities that use various approaches to suit the needs of the client wanting Long-Term Recovery. Evidence based, 12-step based, christian based, and alternative healing based.

```html
<!DOCTYPE html>
<html lang="en">
<head>
<meta charset="utf-8">
<title>Harbor Wellness Partners — Postcard</title>
<link rel="stylesheet" href="https://fonts.googleapis.com/css2?family=Cinzel:wght@400;500&family=Arimo:wght@400&family=Old+Standard+TT:wght@400&display=swap">
<style>
  :root {
    --canvas: #d9d9d9;
    --paper: #ffffff;
    --ink: #111111;
    --black: #0b0b0b;
    --accent: #e0161d;
    --body: #1e1e1e;
    --rule: #222222;
    --photo-light: #efece8;
    --photo-mid: #cdbfb3;
  }
  * { box-sizing: border-box; margin: 0; padding: 0; }
  html, body { width: 1200px; height: 1200px; overflow: hidden; }
  body {
    background: radial-gradient(ellipse at 50% 40%, #f4f4f4 0%, var(--canvas) 100%);
    position: relative;
    font-family: "Arimo", Arial, sans-serif;
    color: var(--ink);
  }
  .card { position: absolute; background: var(--paper); overflow: hidden; box-shadow: 0 2px 6px rgba(0,0,0,.25); }
  .card-front { left: 79px; top: 42px; width: 697px; height: 537px; }
  .card-back { left: 428px; top: 620px; width: 697px; height: 539px; }
  .card svg.shapes { position: absolute; inset: 0; }

  .brand { position: absolute; display: flex; align-items: center; }
  .brand-dot { border-radius: 50%; background: var(--black); flex: none; }
  .brand-divider { background: var(--rule); flex: none; }
  .brand-name {
    font-family: "Old Standard TT", "Times New Roman", serif;
    text-transform: uppercase; color: var(--ink); letter-spacing: .2px;
  }

  /* front */
  .card-front .brand { left: 28px; top: 26px; }
  .card-front .brand-dot { width: 94px; height: 94px; margin-right: 12px; }
  .card-front .brand-divider { width: 1.5px; height: 132px; margin-right: 11px; }
  .card-front .brand-name { font-size: 27px; line-height: 24px; padding-bottom: 6px; }

  .headline { position: absolute; left: 28px; top: 186px; font-family: "Cinzel", serif; }
  .headline-call { font-size: 31px; color: var(--ink); letter-spacing: .3px; line-height: 36px; }
  .headline-sub { font-size: 20px; color: var(--accent); letter-spacing: .6px; line-height: 26px; }
  .front-copy { position: absolute; left: 29px; top: 273px; width: 345px; font-size: 13px; line-height: 17px; color: var(--body); }
  .front-copy p + p { margin-top: 17px; }
  .front-footer { position: absolute; left: 29px; top: 476px; color: #fff; }
  .front-footer .approach { font-size: 13.5px; line-height: 18px; }
  .front-footer .more { font-size: 13.5px; line-height: 22px; margin-top: 6px; white-space: nowrap; }
  .front-footer .more a { color: var(--accent); text-decoration: none; }

  /* back */
  .back-heading { position: absolute; left: 23px; top: 228px; font-family: "Cinzel", serif; color: #fff; }
  .back-heading .line-1 { font-size: 15px; letter-spacing: .5px; line-height: 20px; }
  .back-heading .line-2 { font-size: 19.5px; letter-spacing: 1px; line-height: 28px; }
  .services { position: absolute; left: 24px; top: 286px; list-style: none; color: #fff; font-size: 14px; }
  .services li { height: 24px; display: flex; align-items: center; }
  .services svg { margin-right: 11px; }
  .back-contact { position: absolute; left: 22px; top: 461px; color: #fff; font-size: 14px; line-height: 28px; white-space: nowrap; }
  .card-back .brand { left: 362px; top: 16px; }
  .card-back .brand-dot { width: 56px; height: 56px; margin-right: 6px; }
  .card-back .brand-divider { width: 1.5px; height: 80px; margin-right: 7px; }
  .card-back .brand-name { font-size: 16px; line-height: 14.5px; }
  .stamp { position: absolute; left: 574px; top: 28px; width: 100px; height: 94px; border: 2px solid var(--ink); }
  .address-line { position: absolute; left: 380px; width: 298px; height: 2px; background: var(--ink); }
</style>
</head>
<body>

<section class="card card-front">
  <svg class="shapes" width="697" height="537" viewBox="0 0 697 537">
    <defs>
      <clipPath id="hands-clip"><circle cx="740" cy="290" r="320"/></clipPath>
      <linearGradient id="hands-tone" x1="0" y1="0" x2="1" y2="1">
        <stop offset="0" stop-color="var(--photo-light)"/>
        <stop offset="1" stop-color="var(--photo-mid)"/>
      </linearGradient>
    </defs>
    <rect class="footer-band" x="0" y="459" width="697" height="78" fill="var(--black)"/>
    <circle cx="740" cy="290" r="328" fill="none" stroke="var(--accent)" stroke-width="6"/>
    <circle cx="740" cy="290" r="322" fill="none" stroke="var(--black)" stroke-width="2.5"/>
    <rect x="400" y="0" width="297" height="537" fill="url(#hands-tone)" clip-path="url(#hands-clip)"
          role="img" aria-label="Photo of one hand reaching down to help another open hand"/>
  </svg>

  <div class="brand">
    <span class="brand-dot"></span>
    <span class="brand-divider"></span>
    <span class="brand-name">Harbor<br>Wellness<br>Partners</span>
  </div>

  <div class="headline">
    <div class="headline-call">Call 1-855-HARBR22</div>
    <div class="headline-sub">Before you have to call 911</div>
  </div>

  <div class="front-copy">
    <p>Lorem ipsum dolor sit amet, consectetuer adipiscing elit, sed diam nonummy nibh euismod tincidunt ut laoreet dolore magna aliquam erat volutpat.</p>
    <p>Ut wisi enim ad minim veniam, quis nostrud exerci tation ullamcorper suscipit lobortis nisl ut aliquip ex ea commodo consequat. Duis autem vel eum iriure dolor in hendrerit in vulputate velit esse molestie consequat, vel illum.</p>
  </div>

  <div class="front-footer">
    <div class="approach">Several facilities with several approaches to treatment &amp; recovery.</div>
    <div class="more">For More Information visit <a>www.harborwellnesspartners-demo.com</a></div>
  </div>
</section>

<section class="card card-back">
  <svg class="shapes" width="697" height="539" viewBox="0 0 697 539">
    <defs>
      <linearGradient id="summit-tone" x1="0" y1="0" x2="0" y2="1">
        <stop offset="0" stop-color="#f3f0d8"/>
        <stop offset="0.6" stop-color="#d9c36a"/>
        <stop offset="1" stop-color="#3a3424"/>
      </linearGradient>
      <linearGradient id="support-tone" x1="0" y1="0" x2="1" y2="1">
        <stop offset="0" stop-color="#f6f3f0"/>
        <stop offset="1" stop-color="#c9b3a3"/>
      </linearGradient>
    </defs>
    <path class="black-panel" d="M0 0 H320 C368 170 372 360 318 539 H0 Z" fill="var(--black)"/>
    <path d="M326 0 C374 170 378 362 324 539" fill="none" stroke="var(--black)" stroke-width="2"/>
    <circle cx="105" cy="104" r="84" fill="url(#summit-tone)" stroke="#fff" stroke-width="3"
            role="img" aria-label="Photo of a person with raised arms standing on a summit at sunrise"/>
    <circle cx="231" cy="135" r="72" fill="url(#support-tone)" stroke="#fff" stroke-width="4"
            role="img" aria-label="Photo of a woman comforting a friend"/>
  </svg>

  <div class="back-heading">
    <div class="line-1">Long-Term recovery is our goal,</div>
    <div class="line-2">Not temporary sobriety</div>
  </div>

  <ul class="services">
    <li><svg width="9" height="8" viewBox="0 0 9 8"><path d="M1 4 L3.5 6.5 L8 1.5" fill="none" stroke="#fff" stroke-width="1.8"/></svg>Interventions</li>
    <li><svg width="9" height="8" viewBox="0 0 9 8"><path d="M1 4 L3.5 6.5 L8 1.5" fill="none" stroke="#fff" stroke-width="1.8"/></svg>Detox</li>
    <li><svg width="9" height="8" viewBox="0 0 9 8"><path d="M1 4 L3.5 6.5 L8 1.5" fill="none" stroke="#fff" stroke-width="1.8"/></svg>Partial Hospitalization Program (PHP)</li>
    <li><svg width="9" height="8" viewBox="0 0 9 8"><path d="M1 4 L3.5 6.5 L8 1.5" fill="none" stroke="#fff" stroke-width="1.8"/></svg>Intensive Out Patient (IOP)</li>
    <li><svg width="9" height="8" viewBox="0 0 9 8"><path d="M1 4 L3.5 6.5 L8 1.5" fill="none" stroke="#fff" stroke-width="1.8"/></svg>Out Patient (OP)</li>
    <li><svg width="9" height="8" viewBox="0 0 9 8"><path d="M1 4 L3.5 6.5 L8 1.5" fill="none" stroke="#fff" stroke-width="1.8"/></svg>Sober Living Communities.</li>
  </ul>

  <div class="back-contact">
    <div>Call: 855-HARBR22 (855-427-2722)</div>
    <div>Visit: www.harborwellnesspartners-demo.com</div>
  </div>

  <div class="brand">
    <span class="brand-dot"></span>
    <span class="brand-divider"></span>
    <span class="brand-name">Harbor<br>Wellness<br>Partners</span>
  </div>

  <div class="stamp"></div>
  <div class="address-line" style="top:264px"></div>
  <div class="address-line" style="top:314px"></div>
  <div class="address-line" style="top:364px"></div>
  <div class="address-line" style="top:414px"></div>
</section>

</body>
</html>
```